Business Card Design

I would like a new business card design for an accounting firm that specializes in resolving clients tax problems. I want the card to give the impression that we are not your typical stodgy accounting firm, but at the same time we will get the job done.
Industry/Entity Type
Business
Contact Information for Business Card
Dorian T Welsby
Certified Public Accountant
38-27 52nd Street
Sunnyside, NY 11287
Tel: (718) 555-0142
Fax: (888) 555-0199
e-mail: dtwthecpa@ledgerpost.com
website: harborfilingreliefexperts.com

```html
<!DOCTYPE html>
<html lang="en">
<head>
<meta charset="utf-8">
<title>Dorian T Welsby – Business Card</title>
<link rel="stylesheet" href="https://fonts.googleapis.com/css2?family=Bebas+Neue&display=swap">
<style>
  :root {
    --backdrop: #2b2e36;
    --brand-red: #8e1f1f;
    --card-white: #f4f4f4;
    --ink-gray: #5a5a5a;
    --subtitle-gray: #6b6b6b;
    --name-white: #ffffff;
  }
  * { margin: 0; padding: 0; box-sizing: border-box; }
  html, body {
    width: 1200px; height: 900px; overflow: hidden;
    background: var(--backdrop);
    font-family: "Bebas Neue", "Oswald", sans-serif;
  }
  .card {
    position: absolute; left: 75px; top: 150px;
    width: 1050px; height: 600px;
    display: flex;
    background: var(--card-white);
    box-shadow: 0 18px 40px rgba(0,0,0,.45);
  }
  .card__brand {
    width: 500px; height: 100%;
    background: var(--brand-red);
    position: relative;
  }
  .identity {
    position: absolute; left: 48px; bottom: 150px; width: 430px;
  }
  .identity__name {
    color: var(--name-white);
    font-size: 86px; line-height: .9; letter-spacing: 1px;
    font-weight: 400;
    padding-bottom: 6px;
    border-bottom: 5px solid var(--name-white);
  }
  .identity__title {
    color: var(--subtitle-gray);
    font-size: 43px; line-height: 1.05; letter-spacing: .5px;
    margin-top: 6px; white-space: nowrap;
  }
  .card__contact {
    flex: 1; padding: 52px 30px 0 42px;
    color: var(--ink-gray);
  }
  .contact-group { display: flex; align-items: center; gap: 14px; }
  .contact-group + .contact-group { margin-top: 8px; }
  .contact-group--phone { margin-top: 92px !important; }
  .contact-group--address { margin-top: 92px !important; }
  .contact-icon { width: 40px; height: 40px; flex: none; fill: var(--brand-red); }
  .contact-text { font-size: 29px; line-height: 1.15; letter-spacing: .5px; }
</style>
</head>
<body>
  <main class="card">
    <section class="card__brand">
      <div class="identity">
        <h1 class="identity__name">Dorian T Welsby</h1>
        <p class="identity__title">Certified Public Accountant</p>
      </div>
    </section>

    <section class="card__contact">
      <div class="contact-group">
        <svg class="contact-icon" viewBox="0 0 40 40" aria-hidden="true">
          <path d="M3 15 L20 4 L37 15 V34 H3 Z" fill="none" stroke="#8e1f1f" stroke-width="3"/>
          <path d="M3 15 L20 27 L37 15" fill="none" stroke="#8e1f1f" stroke-width="3"/>
          <circle cx="20" cy="15" r="4" fill="none" stroke="#8e1f1f" stroke-width="2.5"/>
        </svg>
        <span class="contact-text">dtwthecpa@ledgerpost.com</span>
      </div>
      <div class="contact-group">
        <svg class="contact-icon" viewBox="0 0 40 40" aria-hidden="true">
          <rect x="3" y="8" width="34" height="25" rx="3" fill="none" stroke="#8e1f1f" stroke-width="3"/>
          <rect x="8" y="12" width="24" height="17" fill="#8e1f1f"/>
        </svg>
        <span class="contact-text">harborfilingreliefexperts.com</span>
      </div>

      <div class="contact-group contact-group--phone">
        <svg class="contact-icon" viewBox="0 0 40 40" aria-hidden="true">
          <path d="M11 3 L17 11 L13 16 Q16 24 23 28 L28 24 L36 30 L31 37 Q14 35 5 12 Q6 6 11 3 Z"/>
        </svg>
        <span class="contact-text">Tel: (718) 555-0142<br>Fax: (888) 555-0199</span>
      </div>

      <div class="contact-group contact-group--address">
        <svg class="contact-icon" viewBox="0 0 40 48" style="height:48px" aria-hidden="true">
          <path d="M20 2 C10 2 4 9 4 17 C4 28 20 46 20 46 C20 46 36 28 36 17 C36 9 30 2 20 2 Z"/>
          <circle cx="20" cy="17" r="7" fill="none" stroke="#f4f4f4" stroke-width="3"/>
        </svg>
        <span class="contact-text">38-27 52nd Street<br>Sunnyside, NY 11287</span>
      </div>
    </section>
  </main>
</body>
</html>
```